Wanted: A Simple yet Awesome Blog Hero Image

We need a hero image (blog graphic header) to replace our existing one: https://www.brantwellsupply.com//blog/soil-classification-foundation-and-pavement-design-starts-here
Want something to reflect what the blog article is about and is a reflection of the title.

Note: we are not in love with any of our hero graphics

Industry/Entity Type

Construction

Colors

Designer to choose colors to be used in the design.

Requirements
Must have
• Width must be 715px
• Height must not exceed 400px
• Content on graphic should be: Soil Classification: Foundation and Pavement Design Starts Here
Nice to have
• a product shown that is mentioned in the blog
Should not have
• a product with a Carraway logo

```html
<!DOCTYPE html>
<html lang="en">
<head>
<meta charset="utf-8">
<title>Soil Classification: Foundation and Pavement Design Starts Here</title>
<link rel="stylesheet" href="https://fonts.googleapis.com/css2?family=Montserrat:wght@600;700&display=swap">
<style>
  :root {
    --soil-dark: #4a3a27;
    --soil-mid: #6e5a40;
    --soil-light: #8a7559;
    --banner-blue: #2b9ae0;
    --text-white: #ffffff;
  }
  html, body {
    margin: 0;
    padding: 0;
    width: 1200px;
    height: 671px;
    overflow: hidden;
    background: var(--soil-dark);
  }
  .hero {
    position: relative;
    width: 1200px;
    height: 671px;
    overflow: hidden;
    font-family: "Montserrat", Arial, sans-serif;
  }
  .hero__soil {
    position: absolute;
    inset: 0;
    background:
      radial-gradient(ellipse at 30% 40%, rgba(160,140,110,0.35), transparent 60%),
      radial-gradient(ellipse at 80% 70%, rgba(60,45,30,0.45), transparent 60%),
      linear-gradient(135deg, var(--soil-light) 0%, var(--soil-mid) 45%, var(--soil-dark) 100%);
  }
  .hero__banner {
    position: absolute;
    left: 160px;
    top: 159px;
    width: 880px;
    height: 138px;
  }
  .hero__label {
    position: absolute;
    left: 0;
    right: 0;
    top: 159px;
    height: 138px;
    margin: 0;
    display: flex;
    align-items: center;
    justify-content: center;
    color: var(--text-white);
    font-weight: 600;
    font-size: 56px;
    letter-spacing: 0.5px;
  }
  .hero__title {
    position: absolute;
    left: 0;
    right: 0;
    top: 335px;
    margin: 0;
    text-align: center;
    color: var(--text-white);
    font-weight: 700;
    font-size: 59px;
    line-height: 92px;
    text-shadow: 0 2px 6px rgba(0,0,0,0.35);
  }
</style>
</head>
<body>
  <main class="hero">
    <div class="hero__soil" role="img" aria-label="Close-up photograph of dry brown soil with small stones and gravel"></div>
    <svg class="hero__banner" viewBox="0 0 880 138" aria-hidden="true">
      <polygon points="8,0 860,0 880,138 22,138" fill="var(--banner-blue)"/>
    </svg>
    <h2 class="hero__label">SOIL CLASSIFICATION</h2>
    <h1 class="hero__title">Foundation and Pavement<br>Design Starts Here</h1>
  </main>
</body>
</html>
```